Brochure Design - Marketing Document - real estate development

It is a 7 Page Proposal document. Please see attached example. It will be used as a marketing proposal document given to potential clients. It is a 'capability statement' used to demonstrate the capability and expertise of the business. I will provide all images and copy to be used in the document. I just need someone to create the template. Use the attached document as a guide for design, style, look and feel

Company name: Tarvale Living

I'll be happy to receive the document 80% complete so I can fill in the copy and minor details. All I need from a designer is to format and design a template that I can fill in

Thank you!

Target Market(s)

Corporate investors/clients

Font styles to use
Serif
Sans Serif

Requirements
Must have
• Please use the images of elderly people I have uploaded. There doesn't need to be a photo on every page, but please incorporate the images as you see fit. Also please use the logo attached 'Tarvale Living'
• Please see below the template layout/order page by page
• 1st page
• • Branding, photo of beach, headline saying capability statement
• 2nd page
• ABOUT US
• • High level overview from market/retail perspective of what Tarvale offers and who we are
• • Talk about product and company philosophy
• 3rd page
• OUR TEAM
• • Photos, names and roles
• • Speak generally about immense team experience as a composite body of achievement
• 4th Page
• • List of projects and project values
• Page 5
• • More projects and project values
• Page 6
• • What we are offering our JV partners
• • Benefits and options of model
• Page 7
• • How Tarvle will change the market for the better/ difference between us and old models
• Final page
• • Branding, Address, company details. ABN/CAN
Should not have
• Please do NOT use bright/electric colours of blue, green or orange.
• Please use the attached document as a guide for style, colours and layout

```html
<!DOCTYPE html>
<html lang="en">
<head>
<meta charset="utf-8">
<title>Tarvale Living – Proposal Pages 6 and 7</title>
<link rel="stylesheet" href="https://fonts.googleapis.com/css2?family=Arimo:wght@400&family=Cormorant+Garamond:wght@400;500&display=swap">
<style>
  :root {
    --ink: #000000;
    --paper: #ffffff;
    --rule: #9a9a9a;
    --label: #111111;
    --logo-text: #e8e8e8;
  }
  * { margin: 0; padding: 0; box-sizing: border-box; }
  html, body { width: 1200px; height: 848px; overflow: hidden; background: var(--paper); }
  .canvas { position: relative; width: 1200px; height: 848px; background: var(--paper); }

  .page-label {
    position: absolute; top: 16px; width: 200px; text-align: center;
    font-family: "Cormorant Garamond", Georgia, serif; font-size: 31px; font-weight: 500;
    color: var(--label);
  }
  .page-label--six { left: 228px; }
  .page-label--seven { left: 740px; }

  .spread {
    position: absolute; left: 66px; top: 84px; width: 1080px; height: 764px;
    border-top: 1px solid var(--rule); border-left: 1px solid var(--rule); border-right: 1px solid var(--rule);
  }
  .spread__fold { position: absolute; left: 539px; top: 0; bottom: 0; width: 1px; background: var(--rule); }

  .side-column { position: absolute; top: 0; width: 242px; height: 764px; background: var(--ink); }
  .side-column--left { left: 0; }
  .side-column--right { right: 0; }

  .brand { position: absolute; left: 0; top: 0; width: 100%; height: 53px; text-align: center; }
  .brand__name {
    display: block; padding-top: 15px;
    font-family: "Cormorant Garamond", Georgia, serif; font-size: 20px; letter-spacing: 3.4px;
    color: var(--logo-text); font-weight: 400;
  }
  .brand__sub {
    display: block; margin-top: 1px;
    font-family: "Cormorant Garamond", Georgia, serif; font-size: 6px; letter-spacing: 2.6px;
    color: var(--logo-text); font-weight: 400;
  }

  .photo { position: absolute; left: 0; width: 100%; }
  .photo--upper { top: 53px; height: 221px; }
  .photo--lower { top: 490px; height: 274px; }
  .photo--beach-couple { background: linear-gradient(180deg, #2d7fc4 0%, #7fb6df 55%, #e7e4dc 75%, #cdbb9f 100%); }
  .photo--pool { background: linear-gradient(100deg, #9fd0ee 0%, #3a9ad8 40%, #1f6fb6 65%, #c9a48d 88%, #d9c4b6 100%); }
  .photo--cyclist { background: linear-gradient(160deg, #6d8f3a 0%, #9cb566 35%, #e0ddd2 60%, #51703a 100%); }
  .photo--beach-group { background: linear-gradient(180deg, #d7e5f0 0%, #b9d3e6 35%, #d68b78 55%, #e9e4dd 75%, #d9cbb5 100%); }

  .copy {
    font-family: Arimo, Arial, sans-serif; font-size: 10.4px; line-height: 13px; white-space: nowrap;
  }
  .copy p + p { margin-top: 4px; }
  .copy--reverse { position: absolute; left: 30px; color: var(--paper); }
  .copy--reverse.copy--left-column { top: 316px; }
  .copy--reverse.copy--right-column { top: 308px; left: 34px; }
  .copy--main { position: absolute; color: var(--ink); }

  .heading-box {
    position: absolute; background: var(--ink); color: var(--paper); text-align: center;
    font-family: Arimo, Arial, sans-serif; font-weight: 400; font-size: 23px; line-height: 28.3px;
    display: flex; align-items: center; justify-content: center; width: 245px;
  }
  .heading-box--offer { left: 266px; top: 90px; height: 96px; }
  .heading-box--benefits { left: 266px; top: 414px; height: 96px; }
  .heading-box--change { left: 563px; top: 90px; height: 218px; }

  .copy--offer { left: 267px; top: 198px; }
  .copy--benefits { left: 267px; top: 527px; }
  .copy--change { left: 564px; top: 320px; }
</style>
</head>
<body>
<div class="canvas">
  <div class="page-label page-label--six">Page 6</div>
  <div class="page-label page-label--seven">Page 7</div>

  <div class="spread">
    <div class="spread__fold"></div>

    <aside class="side-column side-column--left">
      <div class="brand"><span class="brand__name">TARVALE</span><span class="brand__sub">LIVING</span></div>
      <div class="photo photo--upper photo--beach-couple" role="img" aria-label="Photo: senior couple relaxing together on a sunny beach"></div>
      <div class="copy copy--reverse copy--left-column">
        <p>Nulla lorem eros, hendrerit a mattis<br>vel, elementum aliquam nisi. Etiam<br>vel sapien mi. Cros nec varius ipsum.<br>Interdum et malesuada fames ac ante<br>ipsum primis in faucibus.</p>
        <p>Proin euismod lobortis lacinia.</p>
        <p>Vestibulum velit volutpat dolor tristique<br>fermentum. Etiam commodo, lacus<br>enim lacinla lorem urna sit amet nibh.</p>
      </div>
      <div class="photo photo--lower photo--pool" role="img" aria-label="Photo: senior swimmer standing beside an indoor pool"></div>
    </aside>

    <section class="page-body">
      <h2 class="heading-box heading-box--offer">WHAT WE ARE<br>OFFERING OUR<br>JV PARTNERS</h2>
      <div class="copy copy--main copy--offer">
        <p>Nulla lorem eros, hendrerit a mattis vel,<br>elementum aliquam nisi. Etiam vel sapien mi.<br>Cros nec varius ipsum. Interdum et malesuada<br>fames ac ante ipsum primis in faucibus.</p>
        <p>Proin euismod lobortis lacinia.</p>
        <p>Vestibulum velit volutpat dolor tristique<br>fermentum. Etiam commodo, lacus enim lacinla<br>lorem urna sit amet nibh.</p>
      </div>

      <h2 class="heading-box heading-box--benefits">BENEFITS AND<br>OPTIONS OF MODEL</h2>
      <div class="copy copy--main copy--benefits">
        <p>Nulla lorem eros, hendrerit a mattis vel,<br>elementum aliquam nisi. Etiam vel sapien mi.<br>Cros nec varius ipsum. Interdum et malesuada<br>fames ac ante ipsum primis in faucibus.</p>
        <p>Proin euismod lobortis lacinia.</p>
        <p>Vestibulum velit volutpat dolor tristique<br>fermentum. Etiam commodo, lacus enim lacinla<br>lorem urna sit amet nibh.</p>
      </div>

      <h2 class="heading-box heading-box--change">HOW TARVALE<br>WILL CHANGE<br>THE MARKET<br>FOR THE BETTER/<br>DIFFERENCE<br>BETWEEN US AND<br>OLD MODELS</h2>
      <div class="copy copy--main copy--change">
        <p>Nulla lorem eros, hendrerit a mattis vel,<br>elementum aliquam nisi. Etiam vel sapien mi.<br>Cros nec varius ipsum. Interdum et malesuada<br>fames ac ante ipsum primis in faucibus.</p>
        <p>Proin euismod lobortis lacinia.</p>
        <p>Vestibulum velit volutpat dolor tristique<br>fermentum. Etiam commodo, lacus enim lacinla<br>lorem urna sit amet nibh.</p>
        <p>Nulla lorem eros, hendrerit a mattis vel,<br>elementum aliquam nisi. Etiam vel sapien mi.<br>Cros nec varius ipsum. Interdum et malesuada<br>fames ac ante ipsum primis in faucibus.</p>
        <p>Proin euismod lobortis lacinia.</p>
        <p>Vestibulum velit volutpat dolor tristique<br>fermentum. Etiam commodo, lacus enim lacinla<br>lorem urna sit amet nibh.</p>
        <p>Nulla lorem eros, hendrerit a mattis vel,<br>elementum aliquam nisi. Etiam vel sapien mi.<br>Cros nec varius ipsum. Interdum et malesuada<br>fames ac ante ipsum primis in faucibus.</p>
        <p>Proin euismod lobortis lacinia.</p>
        <p>Vestibulum velit volutpat dolor tristique<br>fermentum. Etiam commodo, lacus enim lacinla<br>lorem urna sit amet nibh.</p>
        <p>Nulla lorem eros, hendrerit a mattis vel,<br>elementum aliquam nisi. Etiam vel sapien mi.</p>
      </div>
    </section>

    <aside class="side-column side-column--right">
      <div class="brand"><span class="brand__name">TARVALE</span><span class="brand__sub">LIVING</span></div>
      <div class="photo photo--upper photo--cyclist" role="img" aria-label="Photo: smiling senior man riding a bicycle through greenery"></div>
      <div class="copy copy--reverse copy--right-column">
        <p>Nulla lorem eros, hendrerit a mattis<br>vel, elementum aliquam nisi. Etiam<br>vel sapien mi. Cros nec varius ipsum.<br>Interdum et malesuada fames ac ante<br>ipsum primis in faucibus.</p>
        <p>Proin euismod lobortis lacinia.</p>
        <p>Vestibulum velit volutpat dolor tristique<br>fermentum. Etiam commodo, lacus<br>enim lacinla lorem urna sit amet nibh.</p>
      </div>
      <div class="photo photo--lower photo--beach-group" role="img" aria-label="Photo: group of seniors in sun hats splashing along the shoreline"></div>
    </aside>
  </div>
</div>
</body>
</html>
```